Lip Balm Label Design

Design a label for a Lavender-Mint lip balm. We make high-quality natural essential oil products. Please use the old label as an example of what exists. The label should include purple. The final design should be eye-catching and distinct. The file should be in an AI file.

Here is the information that should be included on the label:
1) ingredients:Theobroma Cacao (Cocoa) Seed Butter, Theobroma grandiflorum Ultra Refined Butter, beesewax, Calendula Officinalis Flower Oil, Prunus Amygdalus Dulcis (Sweet Almond) Oil, cetyl alcohol and Tocopherol. Lavandula Angustifolia (Lavender) Oil and Mentha Piperita (Peppermint) Oil.

2) www.kelvorascents.com

3) Brand name and logo: K. Velora Aromatherapy (logo is attached- you can use with form)

```html
<!DOCTYPE html>
<html lang="en">
<head>
<meta charset="utf-8">
<title>K. Velora Aromatherapy – Lavender-Mint Lip Balm Label</title>
<link rel="stylesheet" href="https://fonts.googleapis.com/css2?family=Cinzel:wght@400&family=Arimo:wght@400;700&display=swap">
<style>
  :root {
    --backdrop: #fdf8ef;
    --label-pink: #cb7fb3;
    --label-pink-light: #d894c2;
    --label-pink-deep: #b8679f;
    --peach: #f2b4aa;
    --peach-soft: #f6c7bd;
    --tag-text: #8a3a6e;
    --white: #ffffff;
  }
  * { box-sizing: border-box; margin: 0; padding: 0; }
  html, body {
    width: 1200px; height: 909px; overflow: hidden;
    background: var(--backdrop);
  }
  .canvas {
    position: relative; width: 1200px; height: 909px;
    display: flex; align-items: center; justify-content: center;
  }
  .label {
    position: relative; width: 1040px; height: 600px;
    background: linear-gradient(180deg, var(--label-pink-deep) 0%, var(--label-pink) 18%, var(--label-pink-light) 50%, var(--label-pink) 82%, var(--label-pink-deep) 100%);
    overflow: hidden;
    display: grid; grid-template-rows: 180px 190px 230px;
  }
  .lotus-art {
    position: absolute; left: 0; top: 0; width: 190px; height: 600px;
    background: linear-gradient(90deg, var(--peach) 0%, var(--peach-soft) 55%, rgba(246,199,189,0) 100%);
  }
  .row {
    position: relative; display: flex; align-items: center;
    padding-left: 220px; padding-right: 30px;
  }
  .net-weight {
    position: absolute; left: 36px; top: 50%; transform: translateY(-50%);
    font-family: "Cinzel", serif; font-size: 22px; color: var(--white);
    white-space: nowrap;
  }
  .brand { display: flex; align-items: center; gap: 16px; }
  .brand-mark {
    width: 40px; height: 40px; border-radius: 50%;
    border: 2px solid var(--white); flex: none;
  }
  .brand-name {
    font-family: "Cinzel", serif; font-weight: 400; font-size: 40px;
    color: var(--white); letter-spacing: 1px; white-space: nowrap;
  }
  .product-name {
    font-family: "Cinzel", serif; font-weight: 400; font-size: 50px;
    color: var(--white); letter-spacing: 2px; text-transform: uppercase;
    white-space: nowrap;
  }
  .product-type {
    margin-left: 24px; padding: 6px 16px; border-radius: 6px;
    background: var(--peach); color: var(--tag-text);
    font-family: "Cinzel", serif; font-size: 26px; white-space: nowrap;
  }
  .info { max-width: 700px; }
  .ingredients {
    font-family: "Arimo", sans-serif; font-size: 16px;
    line-height: 1.4; color: var(--white); text-align: justify;
  }
  .ingredients strong { font-weight: 700; }
  .website {
    margin-top: 14px; font-family: "Arimo", sans-serif; font-size: 16px;
    font-weight: 700; color: var(--white); letter-spacing: 0.5px;
  }
  .badges { margin-left: auto; display: flex; flex-direction: column; gap: 18px; }
  .badge { width: 44px; height: 44px; border-radius: 50%; border: 3px solid var(--white); }
</style>
</head>
<body>
<main class="canvas">
  <section class="label">
    <div class="lotus-art" role="img" aria-label="Stylised peach lotus flower artwork"></div>

    <div class="row row-brand">
      <span class="net-weight">0.15 Oz</span>
      <div class="brand">
        <span class="brand-mark"></span>
        <h1 class="brand-name">K. Velora Aromatherapy</h1>
      </div>
    </div>

    <div class="row row-product">
      <h2 class="product-name">Lavender-Mint</h2>
      <span class="product-type">Lip Balm</span>
    </div>

    <div class="row row-info">
      <div class="info">
        <p class="ingredients"><strong>INGREDIENTS:</strong> Theobroma Cacao (Cocoa) Seed Butter, Theobroma grandiflorum Ultra Refined Butter, beesewax, Calendula Officinalis Flower Oil, Prunus Amygdalus Dulcis (Sweet Almond) Oil, cetyl alcohol and Tocopherol. Lavandula Angustifolia (Lavender) Oil and Mentha Piperita (Peppermint) Oil.</p>
        <p class="website">www.kelvorascents.com</p>
      </div>
      <div class="badges">
        <span class="badge" role="img" aria-label="Certification badge"></span>
        <span class="badge" role="img" aria-label="Certification badge"></span>
      </div>
    </div>
  </section>
</main>
</body>
</html>
```